2 Large Postcard Designs

I need two large postcards (11' by 9') designed to target two different local business owner markets to entice them both to try the BloomNest marketing platform free for 30 days. (US only target)

Each postcard has to speak to that local business owner both graphically and tone-wise. I have some copy that can be resused and modified. Also the graphic have to be in keeping with BloomNest's brand (go to our website @www.bloomnestcom)

Postcard #1: Targets Local Martial Art Studio Owners

Postcard #2 Targets Local Caterers

Target Market(s)

Local caterer owner and local martial arts studio owner

Industry/Entity Type

Marketing

Requirements
Must have
• REMEMBER THESE ARE TWO SEPARATE POSTCARDS WITH THE SAME OFFER

Front Cover Text options:

What if you could simply click a button and add more customers to your (pick one business here)(martial arts ) /( catering) business?

Back of Postcard:
Well, now you can! (button with BloomNest.com)

Text:
BloomNest is a local marketing solution partner that helps local businesses like yours to grow by building a custom marketing plan and providing an all-in-one platform to get it done easily. We free you up to focus on running your business.

Offer: Try BloomNest's all-in-one marketing platform free for 30 days and get your custom marketing plan to grow your business.
Call or click today at www.bloomnest.com/free-trial
(Caterer number) 1-877-555-0148
(Martial Arts number) (1-855-555-0193)
Nice to have
• You can try to use the uploaded art we have bought if they work for your design, but I am open too new designs
Should not have
• These should look professional and not too techie. They should not be too dark or black. They should get your attention in a professional way.

```html
<!DOCTYPE html>
<html lang="en">
<head>
<meta charset="utf-8">
<title>Martial Arts Postcard – Front</title>
<link rel="stylesheet" href="https://fonts.googleapis.com/css2?family=Roboto:wght@300;400&display=swap">
<style>
  :root {
    --paper: #ffffff;
    --frame: #8a8a8a;
    --ink: #333333;
    --accent-orange: #d3612b;
    --accent-blue: #1f4f8b;
  }
  html, body {
    margin: 0;
    padding: 0;
    width: 989px;
    height: 1200px;
    overflow: hidden;
    background: var(--paper);
  }
  .postcard {
    position: relative;
    width: 989px;
    height: 1200px;
    background: var(--paper);
    font-family: "Roboto", "Helvetica Neue", Arial, sans-serif;
    font-weight: 300;
  }
  .postcard__frame {
    position: absolute;
    left: 25px;
    top: 20px;
    width: 937px;
    height: 1160px;
    border: 1px solid var(--frame);
    box-sizing: border-box;
  }
  .headline__line {
    position: absolute;
    margin: 0;
    line-height: 1;
    white-space: nowrap;
    text-transform: uppercase;
    letter-spacing: -1px;
  }
  .headline__lead {
    position: absolute;
    left: 236px;
    top: 122px;
    margin: 0;
    font-size: 25px;
    line-height: 1;
    color: var(--ink);
    white-space: nowrap;
  }
  .headline__line--add { left: 212px; top: 153px; font-size: 104px; color: var(--accent-orange); }
  .headline__line--customers { left: 98px; top: 258px; font-size: 104px; color: var(--accent-blue); }
  .headline__connector {
    position: absolute;
    left: 722px;
    top: 285px;
    font-size: 25px;
    line-height: 1;
    color: var(--accent-blue);
    white-space: nowrap;
  }
  .headline__line--trade { left: 212px; top: 357px; font-size: 104px; color: var(--accent-orange); }
  .headline__line--business { left: 336px; top: 452px; font-size: 104px; color: var(--accent-blue); }
  .belt-row {
    position: absolute;
    left: 48px;
    top: 612px;
    width: 900px;
    height: 462px;
    background: linear-gradient(90deg,
      #ececec 0%, #ececec 10%,
      #e3c21f 16%, #e3c21f 24%,
      #df6a1e 31%, #df6a1e 38%,
      #2f7d32 45%, #2f7d32 52%,
      #1e5fb3 59%, #1e5fb3 66%,
      #7a4a25 73%, #7a4a25 81%,
      #2a2a2a 88%, #2a2a2a 100%);
  }
</style>
</head>
<body>
  <main class="postcard">
    <div class="postcard__frame"></div>
    <h1 class="headline">
      <span class="headline__lead">What if you could simply click a button &amp;</span>
      <span class="headline__line headline__line--add">Add More</span>
      <span class="headline__line headline__line--customers">Customers</span>
      <span class="headline__connector">to your</span>
      <span class="headline__line headline__line--trade">Martial Arts</span>
      <span class="headline__line headline__line--business">Business ?</span>
    </h1>
    <div class="belt-row" role="img" aria-label="Row of seven folded martial arts belts in white, yellow, orange, green, blue, brown and black"></div>
  </main>
</body>
</html>
```